Dance Card to Provide Contact Info

I'm looking for a double sided business card to provide contact information to perspective dance partners.
One side of the card would have the words: "Yes I would love to Dance" written in an interesting and eye catching way. Below that would be the three categories I'm interested in
>Social >Exhibition >Competition
The other side of the card would include a picture of me with my Name, Phone Number, and Email Address (Dale Pruitt, 210-574-1328, dale@twirlnstep.dance)
My target market is middle aged women interested in Country and Western dancing and West Coast Swing dancing. I am NOT particularly interested in Ballroom style.
Here are a few links to the type of dancing I want to do:
http://www.plvkrn.org/
http://www.prairiefolkstepsociety.com/
http://mesquitevalleytwostep.com/
Dale Pruitt
210-574-1328
dale@twirlnstep.dance

```html
<!DOCTYPE html>
<html lang="en">
<head>
<meta charset="utf-8">
<title>Dale Pruitt — Dance Card</title>
<link href="https://fonts.googleapis.com/css2?family=Montserrat:wght@400;600&display=swap" rel="stylesheet">
<style>
  :root {
    --blue: #1b5a88;
    --orange: #f39a1e;
    --white: #ffffff;
    --stage: #e9ebee;
    --ink: #1b5a88;
    --photo-warm: #d9a488;
    --photo-dark: #2a2a2a;
  }
  * { box-sizing: border-box; margin: 0; padding: 0; }
  html, body { width: 1200px; height: 900px; overflow: hidden; }
  body {
    background: var(--stage);
    font-family: "Montserrat", Arial, sans-serif;
    position: relative;
  }
  .card {
    position: absolute;
    left: 280px;
    width: 640px;
    height: 366px;
    border-radius: 22px;
    overflow: hidden;
    box-shadow: 0 6px 18px rgba(0,0,0,0.18);
  }
  .card-front { top: 68px; background: var(--blue); }
  .card-back { top: 466px; background: var(--white); }
  .card svg.shapes { position: absolute; inset: 0; width: 100%; height: 100%; }

  .headline {
    position: absolute;
    left: 0; right: 0; top: 96px;
    text-align: center;
    color: var(--white);
    font-weight: 400;
  }
  .headline-lead {
    display: block;
    font-size: 29px;
    letter-spacing: 1px;
  }
  .headline-dance {
    display: block;
    font-size: 58px;
    letter-spacing: 4px;
    line-height: 1.15;
    margin-left: 110px;
  }
  .categories {
    position: absolute;
    right: 30px;
    top: 248px;
    color: var(--white);
    font-size: 15px;
    letter-spacing: 0.5px;
  }
  .categories .arrow { color: var(--orange); }

  .photo {
    position: absolute;
    left: 380px; top: 0;
    width: 260px; height: 262px;
    background:
      radial-gradient(ellipse 42% 38% at 42% 34%, var(--photo-warm) 0%, var(--photo-warm) 55%, rgba(217,164,136,0) 100%),
      radial-gradient(ellipse 70% 55% at 62% 100%, var(--photo-dark) 0%, var(--photo-dark) 60%, rgba(42,42,42,0) 100%),
      var(--white);
  }
  .name {
    position: absolute;
    left: 22px; top: 126px;
    display: flex; align-items: center; gap: 10px;
    font-weight: 600;
    font-size: 24px;
    letter-spacing: 1px;
  }
  .name-mark { width: 14px; height: 14px; background: var(--blue); }
  .name-first { color: var(--orange); }
  .name-last { color: var(--ink); }
  .contact {
    position: absolute;
    left: 36px; top: 266px;
    list-style: none;
    color: var(--ink);
    font-size: 17px;
    line-height: 1.45;
  }
  .contact li { display: flex; align-items: center; gap: 10px; }
  .contact svg { width: 14px; height: 14px; flex: none; }
</style>
</head>
<body>

  <section class="card card-front">
    <svg class="shapes" viewBox="0 0 640 366" preserveAspectRatio="none" aria-hidden="true">
      <polygon points="0,314 372,282 400,300 640,276 640,366 0,366" fill="var(--white)"/>
      <polygon points="0,306 372,274 374,282 0,314" fill="var(--orange)"/>
      <polygon points="396,292 640,268 640,276 400,300" fill="var(--orange)"/>
    </svg>
    <h1 class="headline">
      <span class="headline-lead">YES I WOULD LOVE TO</span>
      <span class="headline-dance">DANCE</span>
    </h1>
    <p class="categories">SOCIAL <span class="arrow">&gt;</span>EXHIBITION <span class="arrow">&gt;</span>COMPETITION</p>
  </section>

  <section class="card card-back">
    <div class="photo" role="img" aria-label="Portrait photograph of Dale Pruitt"></div>
    <svg class="shapes" viewBox="0 0 640 366" preserveAspectRatio="none" aria-hidden="true">
      <polygon points="418,262 640,240 640,248 418,270" fill="var(--orange)"/>
      <polygon points="418,270 640,248 640,366 404,366" fill="var(--blue)"/>
      <polygon points="0,350 400,316 402,326 0,362" fill="var(--orange)"/>
    </svg>
    <h2 class="name">
      <span class="name-mark"></span>
      <span><span class="name-first">DALE</span> <span class="name-last">PRUITT</span></span>
    </h2>
    <ul class="contact">
      <li>
        <svg viewBox="0 0 24 24"><path d="M6.6 10.8a15 15 0 0 0 6.6 6.6l2.2-2.2a1 1 0 0 1 1-.25 11.4 11.4 0 0 0 3.6.57 1 1 0 0 1 1 1V20a1 1 0 0 1-1 1A17 17 0 0 1 3 4a1 1 0 0 1 1-1h3.5a1 1 0 0 1 1 1c0 1.25.2 2.45.57 3.6a1 1 0 0 1-.25 1z" fill="var(--orange)"/></svg>
        210-574-1328
      </li>
      <li>
        <svg viewBox="0 0 24 24"><rect x="2" y="5" width="20" height="14" rx="2" fill="none" stroke="var(--orange)" stroke-width="2.4"/><path d="M3 6l9 7 9-7" fill="none" stroke="var(--orange)" stroke-width="2.4"/></svg>
        dale@twirlnstep.dance
      </li>
    </ul>
  </section>

</body>
</html>
```